Wavelume artwork for new single release

I need Wavelume artwork creating to release a new single on there.

The specs are:

Ideal size: 3000 x 3000 pixels
Minimum size: 1400 x 1400 pixels
Aspect ratio: 1:1 (must be a perfect square)
File format: JPG or PNG
Color space: sRGB
File size: Max 4MB

The song is called "Still, Can We Wander?"
The artist is "Milo Fenwright"

We have no images of Milo, so it really is open to imagination.

Target Market(s)

Wavelume listeners

Industry/Entity Type

Music

```html
<!DOCTYPE html>
<html lang="en">
<head>
<meta charset="utf-8">
<title>Milo Fenwright – Still, Can We Wander?</title>
<link rel="stylesheet" href="https://fonts.googleapis.com/css2?family=Chonburi&family=Sora:wght@700&display=swap">
<style>
  :root {
    --sky-top: #e6dfcc;
    --sky-mid: #f1ddb8;
    --glow: #f7b46a;
    --ember: #c8652e;
    --orange: #f36a0a;
    --shade: #2c2623;
    --ink: #1f2328;
    --title: #ffffff;
    --title-shadow: #e0611c;
  }
  html, body {
    margin: 0;
    padding: 0;
    width: 1200px;
    height: 1200px;
    overflow: hidden;
    background: var(--sky-top);
  }
  .cover {
    position: relative;
    width: 1200px;
    height: 1200px;
    overflow: hidden;
  }
  .cover-photo {
    position: absolute;
    inset: 0;
    background:
      radial-gradient(ellipse 200px 170px at 700px 440px, #fff6de 0%, rgba(255,240,210,0.85) 45%, rgba(255,220,170,0) 100%),
      radial-gradient(ellipse 360px 260px at 330px 420px, rgba(44,38,35,0.85) 0%, rgba(44,38,35,0.5) 55%, rgba(44,38,35,0) 100%),
      radial-gradient(ellipse 300px 300px at 1000px 560px, rgba(170,70,40,0.75) 0%, rgba(170,70,40,0) 100%),
      linear-gradient(180deg, var(--sky-top) 0%, var(--sky-mid) 30%, var(--glow) 55%, var(--ember) 75%, var(--orange) 100%);
  }
  .artist-name {
    position: absolute;
    left: 98px;
    top: 110px;
    margin: 0;
    font-family: "Sora", sans-serif;
    font-weight: 700;
    font-size: 54px;
    letter-spacing: 1px;
    line-height: 1;
    color: var(--ink);
    text-transform: uppercase;
  }
  .song-title {
    position: absolute;
    left: 96px;
    top: 735px;
    margin: 0;
    font-family: "Chonburi", serif;
    font-weight: 400;
    font-size: 126px;
    line-height: 120px;
    color: var(--title);
    text-shadow: 4px 4px 0 var(--title-shadow);
  }
  .song-title span { display: block; }
</style>
</head>
<body>
  <main class="cover">
    <div class="cover-photo" role="img" aria-label="Two hands forming a heart shape silhouetted against a glowing orange sunset sky"></div>
    <h2 class="artist-name">Milo Fenwright</h2>
    <h1 class="song-title">
      <span>Still, Can</span>
      <span>We</span>
      <span>Wander?</span>
    </h1>
  </main>
</body>
</html>
```